Harwick Oates - Facebook Cover Photo & Photo Icon Design

We’re looking for a Facebook Cover Photo and Profile Icon design for Harwick Oates, a leading Residential Real Estate brand under Harwick Property Agents, based in Capalaba and Alexandra Hills, Queensland, Australia.

This design will represent my professional real estate profile and needs to be bold, clean, and on-brand.

Deliverables:

Facebook Cover Photo (820 x 312 px, optimized for mobile + desktop)

Facebook Profile Icon (1:1 ratio, minimum 320 x 320 px)

Design Guidelines:

1. Must Include:

The Harwick Oates logo (provided after project start)

Use of the Harwick Property Agents brand colour palette (will be supplied)

Clear connection to residential real estate

2. Optional but Preferred:

A local photo or skyline of Capalaba or Alexandra Hills in QLD (bonus points for this)

Space for a short tagline like:
“Selling Faster. Selling Smarter. Selling Harwick.”
(Optional tagline – open to variations if it improves layout/design)

3. Style & Feel:

Professional yet personable

Clean, modern aesthetic

Subtle touches of fun or personality are welcome

Layout must work well when overlaid by Facebook UI elements (like profile photo & call-to-action buttons)

Who I Am:
I'm a well-known residential real estate agent in the Redlands area, known for high-energy campaigns, premium video marketing, and a results-driven approach. My brand is fun, fresh, and high-performing — just like the real estate campaigns I run.

Files to be Provided (after selection):

Harwick Oates logo in high-res

Brand colour palette / style reference

Optional photo references if local imagery is not sourced by designer

Final Notes:

Make sure all text is legible on mobile and desktop

Original, layered design files must be delivered (PSD or AI preferred)

Bonus points if it feels uniquely “Bayside Queensland” while maintaining a national-level professional polish

Target Market(s)

Alexandra Hills, Capalaba & Sheldon

Industry/Entity Type

Real Estate

Colors
0054AA
0677BA
7BADD7
CADEEF
E8F1F8

Requirements
Must have
• Headshot, Mobile Number 0491 726 055, Suburbs - Alexandra Hills, Capalaba & Sheldon
Nice to have
• White, Crisp & Professional. Bottom Banner with Suburb List. Specialising in Alexandra Hills, Capalaba & Sheldon

```html
<!DOCTYPE html>
<html lang="en">
<head>
<meta charset="utf-8">
<title>Harwick Oates – Cover and Profile Icons</title>
<link rel="stylesheet" href="https://fonts.googleapis.com/css2?family=Raleway:wght@400;500&family=Open+Sans:wght@700&display=swap">
<style>
  :root {
    --page: #d9dadf;
    --navy: #1b2a6b;
    --navy-deep: #0f1a5c;
    --gold: #d4a76a;
    --white: #ffffff;
    --sky-top: #1466d8;
    --sky-mid: #6f97d2;
    --dusk: #e3a591;
    --land: #4b5c45;
  }
  * { margin: 0; padding: 0; box-sizing: border-box; }
  html, body { width: 1200px; height: 684px; overflow: hidden; }
  body {
    background: var(--page);
    position: relative;
    font-family: "Raleway", Arial, sans-serif;
  }

  .cover {
    position: absolute;
    left: 190px; top: 94px;
    width: 820px; height: 312px;
    background: var(--navy);
    overflow: hidden;
  }
  .cover__scene {
    position: absolute;
    left: 330px; top: 0;
    width: 490px; height: 267px;
    background: linear-gradient(to bottom, var(--sky-top) 0%, var(--sky-mid) 42%, var(--dusk) 52%, #5f7a86 56%, var(--land) 66%, #3e4c38 100%);
  }
  .cover__scene::after {
    content: "";
    position: absolute; inset: 0;
    background: linear-gradient(to right, var(--navy) 0%, rgba(27,42,107,0.85) 25%, rgba(27,42,107,0) 60%);
  }
  .cover__agent {
    position: absolute;
    left: 516px; top: 24px;
    width: 246px; height: 243px;
    border-radius: 110px 110px 0 0;
    background: linear-gradient(to bottom, #3b4c66 0%, #34455e 45%, #2e3d55 100%);
  }

  .brand-name {
    position: absolute;
    left: 73px; top: 26px;
    color: var(--white);
    font-weight: 400;
    line-height: 1;
    text-transform: uppercase;
  }
  .brand-name__first { display: block; font-size: 30px; letter-spacing: 3px; margin-left: 40px; }
  .brand-name__last { display: block; font-size: 72px; letter-spacing: 6px; margin-top: 6px; }

  .headline {
    position: absolute;
    left: 73px; top: 135px;
    width: 334px;
    border-top: 1px solid rgba(255,255,255,0.8);
    border-bottom: 1px solid rgba(255,255,255,0.8);
    padding: 8px 0 6px;
    text-transform: uppercase;
    line-height: 1.2;
  }
  .headline__lead { display: block; color: var(--gold); font-size: 24px; font-weight: 500; }
  .headline__main { display: block; color: var(--white); font-size: 27px; font-weight: 400; white-space: nowrap; }

  .region {
    position: absolute;
    left: 73px; top: 223px;
    color: var(--white);
    font-size: 15px;
    font-weight: 500;
    text-transform: uppercase;
  }

  .cover__band {
    position: absolute;
    left: 0; top: 267px;
    width: 820px; height: 45px;
  }
  .suburbs {
    position: absolute;
    left: 0; top: 267px;
    width: 550px; height: 45px;
    line-height: 45px;
    text-align: center;
    color: var(--navy);
    font-size: 15px;
    font-weight: 500;
    text-transform: uppercase;
  }
  .contact {
    position: absolute;
    left: 568px; top: 267px;
    height: 45px;
    display: flex; align-items: center; gap: 9px;
    color: var(--navy);
    font-family: "Open Sans", Arial, sans-serif;
    font-weight: 700;
    font-size: 23px;
  }

  .profile-icon {
    position: absolute;
    top: 460px;
    width: 143px; height: 143px;
    border-radius: 50%;
    border: 4px solid;
    display: flex; flex-direction: column; align-items: center; justify-content: center;
    font-weight: 400;
    text-transform: uppercase;
    line-height: 1;
  }
  .profile-icon--navy { left: 431px; background: var(--navy-deep); border-color: var(--gold); color: var(--white); }
  .profile-icon--gold { left: 627px; background: var(--gold); border-color: var(--navy-deep); color: var(--navy-deep); }
  .profile-icon__first { font-size: 13px; letter-spacing: 1px; }
  .profile-icon__last { font-size: 30px; letter-spacing: 2px; margin-top: 4px; }
</style>
</head>
<body>
  <section class="cover">
    <div class="cover__scene" role="img" aria-label="Aerial photo of bayside suburbs at dusk with blue sky and sea horizon"></div>
    <div class="cover__agent" role="img" aria-label="Headshot of the agent in a dark suit and white shirt"></div>

    <div class="brand-name">
      <span class="brand-name__first">Harwick</span>
      <span class="brand-name__last">Oates</span>
    </div>

    <div class="headline">
      <span class="headline__lead">Clear connection to</span>
      <span class="headline__main">Residential real estate</span>
    </div>

    <p class="region">Bayside Queensland</p>

    <svg class="cover__band" viewBox="0 0 820 45" width="820" height="45" aria-hidden="true">
      <rect x="0" y="0" width="820" height="45" fill="#ffffff"/>
      <polygon points="0,0 557,0 535,45 0,45" fill="#d4a76a"/>
      <line x1="559" y1="0" x2="537" y2="45" stroke="#1b2a6b" stroke-width="2.5"/>
    </svg>
    <p class="suburbs">Specialising in Alexandra Hills, Capalaba &amp; Sheldon</p>
    <div class="contact">
      <svg width="24" height="24" viewBox="0 0 24 24" aria-hidden="true">
        <path d="M6.6 2.5l3 3.6-1.8 2.4c1.2 2.6 3.1 4.5 5.7 5.7l2.4-1.8 3.6 3-1.7 3.3c-7.5-.6-13.9-7-14.5-14.5z" fill="none" stroke="#d4a76a" stroke-width="1.8" stroke-linejoin="round"/>
        <path d="M14 3.5a7 7 0 0 1 6.5 6.5M14 7a3.5 3.5 0 0 1 3 3" fill="none" stroke="#d4a76a" stroke-width="1.6" stroke-linecap="round"/>
      </svg>
      <span>0491 726 055</span>
    </div>
  </section>

  <div class="profile-icon profile-icon--navy">
    <span class="profile-icon__first">Harwick</span>
    <span class="profile-icon__last">Oates</span>
  </div>
  <div class="profile-icon profile-icon--gold">
    <span class="profile-icon__first">Harwick</span>
    <span class="profile-icon__last">Oates</span>
  </div>
</body>
</html>
```